Business Card Design

Please visit www.MarkDorsey.com to acquire information for business card.

Back Side of Card:
a lifetime of experience working for you.

With over 25 years in the construction industry, well over a decade as a licensed Subcontractor / General Contractor and nearly 10 years as a licensed Realtor, I have excelled and cultivated a working knowledge of how all the pieces fit together.

Here is a link to folder.
https://files.examplecloud.net/folderview?id=7Qk2mXrTpLw9zVbN4sHcDyUeFaGj&usp=sharing

Industry/Entity Type

Construction

Contact Information for Business Card

Company: Mark Dorsey, LLC.
Address: 31872 W. Cedar Hollow Blvd. Suite 207-418
Name: Mark Dorsey
Phone: (623) 587-2914
Web: www.MarkDorsey.com
Type of services offered: Architectural Design, 3D Models, Renderings & Animation - Construction Documents - Project Managment.

```html
<!DOCTYPE html>
<html lang="en">
<head>
<meta charset="utf-8">
<title>Mark Dorsey, LLC. — Business Card</title>
<link rel="stylesheet" href="https://fonts.googleapis.com/css2?family=Questrial&display=swap">
<style>
  :root {
    --backdrop: #5d6869;
    --card: #1c2021;
    --accent: #3a82f0;
    --band-text: #0d1112;
    --muted: #6f7678;
  }
  * { margin: 0; padding: 0; box-sizing: border-box; }
  html, body {
    width: 1200px;
    height: 741px;
    overflow: hidden;
    background: var(--backdrop);
    font-family: "Questrial", "Helvetica Neue", Arial, sans-serif;
  }
  .stage {
    position: relative;
    width: 1200px;
    height: 741px;
  }
  .card {
    position: absolute;
    left: 400px;
    width: 409px;
    height: 238px;
    background: var(--card);
    overflow: hidden;
  }
  .card--front { top: 89px; }
  .card--back { top: 413px; }

  .company-name {
    position: absolute;
    left: 0;
    right: 0;
    top: 96px;
    text-align: center;
    color: var(--accent);
    font-size: 39px;
    line-height: 1;
    letter-spacing: 0.5px;
    font-weight: 400;
  }

  .person-name {
    position: absolute;
    left: 27px;
    top: 43px;
    color: var(--accent);
    font-size: 27px;
    line-height: 1;
    font-weight: 400;
  }

  .services-band {
    position: absolute;
    left: 0;
    right: 0;
    top: 96px;
    height: 69px;
    background: var(--accent);
    color: var(--band-text);
    font-size: 11.6px;
    line-height: 18px;
    padding-top: 16px;
  }
  .services-band .line { display: block; white-space: nowrap; }
  .services-band .line--one { padding-left: 31px; }
  .services-band .line--two { padding-left: 52px; }

  .contact-item {
    position: absolute;
    display: flex;
    align-items: center;
    gap: 9px;
    color: var(--muted);
    font-size: 12.8px;
    letter-spacing: 0.6px;
    white-space: nowrap;
    line-height: 1;
  }
  .contact-item svg { width: 12px; height: 12px; flex: none; fill: var(--accent); }
  .contact-item--phone { left: 31px; top: 196px; }
  .contact-item--web { left: 200px; top: 196px; }
  .contact-item--address { left: 31px; top: 218px; }
  .address-suite { margin-left: 10px; }
</style>
</head>
<body>
<main class="stage">
  <section class="card card--front" aria-label="Card front">
    <h1 class="company-name">Mark Dorsey, LLC.</h1>
  </section>

  <section class="card card--back" aria-label="Card back">
    <h2 class="person-name">Mark Dorsey</h2>

    <p class="services-band">
      <span class="line line--one">Architectural Design, 3D Models, Renderings &amp; Animation</span>
      <span class="line line--two">Construction Documents - Project Managment.</span>
    </p>

    <p class="contact-item contact-item--phone">
      <svg viewBox="0 0 24 24" aria-hidden="true"><path d="M6.6 10.8a15.1 15.1 0 0 0 6.6 6.6l2.2-2.2c.3-.3.7-.4 1-.2 1.1.4 2.3.6 3.6.6.6 0 1 .4 1 1V20c0 .6-.4 1-1 1A17 17 0 0 1 3 4c0-.6.4-1 1-1h3.5c.6 0 1 .4 1 1 0 1.3.2 2.5.6 3.6.1.3 0 .7-.2 1z"/></svg>
      <span>(623) 587-2914</span>
    </p>

    <p class="contact-item contact-item--web">
      <svg viewBox="0 0 24 24" aria-hidden="true"><path d="M12 2a10 10 0 1 0 0 20 10 10 0 0 0 0-20zm-1 17.9A8 8 0 0 1 4.1 10l4.9 4.9v1a2 2 0 0 0 2 2zm6.9-2.5a2 2 0 0 0-1.9-1.4h-1v-3a1 1 0 0 0-1-1H8v-2h2a1 1 0 0 0 1-1V7h2a2 2 0 0 0 2-2v-.4a8 8 0 0 1 2.9 12.8z"/></svg>
      <span>www.MarkDorsey.com</span>
    </p>

    <p class="contact-item contact-item--address">
      <svg viewBox="0 0 24 24" aria-hidden="true"><path d="M12 2a7 7 0 0 0-7 7c0 5.2 7 13 7 13s7-7.8 7-13a7 7 0 0 0-7-7zm0 9.5a2.5 2.5 0 1 1 0-5 2.5 2.5 0 0 1 0 5z"/></svg>
      <span>31872 W. Cedar Hollow Blvd.<span class="address-suite">Suite 207-418</span></span>
    </p>
  </section>
</main>
</body>
</html>
```